Architectural Design Build company needs a direct mail flyer

We are a fully service Design Build company who specialize in luxury custom and pre-designed new homes and major home renovations. Our team consists of seasoned architectural, interior design and general contracting professionals all under one roof. We offer clients a transparent, streamlined process to maximize their investment and completion on a timely basis. Leveraging photography and a few before and after and also our Best Builder Awards.

Target Market(s)

Homeowners and buyers between 40-60 years old and financial investment of $300k or more for renovations and $1,000,000 or more for new construction.

Industry/Entity Type

homebuilding and renovations

Colors

Designer to choose colors to be used in the design.

Requirements
Must have
• The construction segments we are focusing this mailer on are transformative renovations and professionally designed custom new homes. . Should have the Pelwick Before kitchen and after as well as the exterior before and after. and new construction elevation photos.
Nice to have
• WOuld like to see two befores and afters highlighted, mention that are architect and designer are part of the team from start to finish,

```html
<!DOCTYPE html>
<html lang="en">
<head>
<meta charset="utf-8">
<title>Varne Design Build – Direct Mail Flyer</title>
<link rel="stylesheet" href="https://fonts.googleapis.com/css2?family=Outfit:wght@400;500;700;800&display=swap">
<style>
  :root{
    --backdrop:#ececec;
    --paper:#f7f7f7;
    --charcoal:#2a2826;
    --panel:#3a3a37;
    --lime:#cdf25a;
    --white:#ffffff;
    --ink:#1f1f1f;
    --muted:#4a4a4a;
  }
  *{margin:0;padding:0;box-sizing:border-box}
  html,body{width:1034px;height:1200px;overflow:hidden;background:var(--backdrop);font-family:"Outfit",sans-serif}
  .flyer{position:absolute;left:92px;top:0;width:850px;height:1200px;background:var(--paper);overflow:hidden}
  .flyer-art{position:absolute;inset:0;width:850px;height:1200px}
  .abs{position:absolute}
  .brand{font-weight:800;letter-spacing:.12em;color:var(--white)}
  .brand-top{left:52px;top:92px;font-size:23px}
  .headline{left:52px;top:136px;color:var(--white);font-weight:800;font-size:37px;line-height:41px;text-transform:uppercase}
  .tagline{left:54px;top:268px;color:#e8e8e8;font-size:14px;line-height:21px;font-weight:400}
  .project-title{font-weight:800;font-size:19px;color:var(--ink);text-transform:uppercase}
  .project-caption{font-size:7.5px;color:var(--muted)}
  .compare{display:flex;clip-path:polygon(0 0,93% 0,100% 8%,100% 92%,96% 100%,0 100%)}
  .compare-photo{position:relative;flex:1;height:100%}
  .compare-photo + .compare-photo{border-left:2px solid var(--white)}
  .compare-label{position:absolute;bottom:8px;left:0;right:0;text-align:center;color:var(--white);font-weight:700;font-size:12px}
  .compare-handle{position:absolute;left:50%;top:50%;width:20px;height:20px;margin:-10px 0 0 -10px;border-radius:50%;background:var(--white);font-size:8px;line-height:20px;text-align:center;color:var(--ink)}
  .kitchen-before{background:linear-gradient(160deg,#6d4a35,#3b2a20 55%,#1c1714)}
  .kitchen-after{background:linear-gradient(170deg,#f4f4f2,#d9dbd8 55%,#555 100%)}
  .exterior-before{background:linear-gradient(165deg,#e8e9e7,#9a9c98 50%,#2b2b2b)}
  .exterior-after{background:linear-gradient(180deg,#d9d4c8 0%,#6d6a60 35%,#4e8a34 60%,#3b2f26 100%)}
  .banner-title{left:44px;top:990px;font-weight:800;font-size:22px;line-height:28px;color:var(--ink);text-transform:uppercase}
  .banner-body{left:44px;top:1056px;font-size:9.5px;line-height:13px;color:var(--ink)}
  .process-title{left:372px;top:555px;width:443px;text-align:center;color:var(--white);font-weight:700;font-size:15.5px;line-height:20px;text-transform:uppercase}
  .step{color:var(--white);width:130px}
  .step-left{text-align:right}
  .step-name{font-weight:700;font-size:8px;text-transform:uppercase}
  .step-time{font-size:6px;margin:2px 0 5px}
  .step-text{font-size:6.2px;line-height:8.5px;color:#d9d9d9}
  .brand-bottom{left:0;width:850px;top:1128px;text-align:center;font-size:46px;color:var(--charcoal);letter-spacing:.1em}
  .contact{color:var(--white);font-size:13px;top:1178px;display:flex;align-items:center;gap:9px}
  .contact-email{left:62px}
  .contact-phone{left:633px}
</style>
</head>
<body>
<main class="flyer">
  <svg class="flyer-art" viewBox="0 0 850 1200" aria-hidden="false">
    <defs>
      <linearGradient id="homeTones" x1="0" y1="0" x2="1" y2="1">
        <stop offset="0" stop-color="#9fb6c7"/>
        <stop offset=".35" stop-color="#e9e7e1"/>
        <stop offset=".65" stop-color="#8a7f6a"/>
        <stop offset="1" stop-color="#3e4a37"/>
      </linearGradient>
    </defs>
    <polygon class="header-shape" points="0,0 812,0 379,450 351,460 0,365" fill="var(--charcoal)"/>
    <polygon role="img" aria-label="Photo of a newly built white two-storey custom home with a covered front porch" points="812,0 850,0 850,650 815,640 379,450 465,330" fill="url(#homeTones)"/>
    <polygon class="accent-stripe" points="800,0 820,4 468,328 452,328" fill="var(--lime)"/>
    <polygon class="accent-corner" points="815,610 850,598 850,656 815,640" fill="var(--lime)"/>
    <polygon class="process-panel" points="372,440 815,553 815,1029 372,1085" fill="var(--panel)"/>
    <polygon class="cta-banner" points="8,940 352,940 281,1122 8,1122" fill="var(--lime)"/>
    <polygon class="footer-bar" points="8,1172 268,1172 293,1200 8,1200" fill="var(--charcoal)"/>
    <polygon class="footer-bar" points="566,1200 592,1172 850,1172 850,1200" fill="var(--charcoal)"/>

    <g class="timeline">
      <path d="M557,648 C557,682 629,662 629,698 C629,732 557,710 557,745 C557,780 629,756 629,791 C629,826 557,806 557,840 C557,874 629,852 629,887 C629,922 557,900 557,935 C557,970 629,948 629,982"
            fill="none" stroke="var(--lime)" stroke-width="4"/>
      <g fill="var(--panel)" stroke="#8a9a40" stroke-width="1" stroke-dasharray="2 2">
        <circle cx="557" cy="648" r="28"/><circle cx="629" cy="698" r="28"/>
        <circle cx="557" cy="745" r="28"/><circle cx="629" cy="791" r="28"/>
        <circle cx="557" cy="840" r="28"/><circle cx="629" cy="887" r="28"/>
        <circle cx="557" cy="935" r="28"/><circle cx="629" cy="982" r="28"/>
      </g>
      <g fill="none" stroke="var(--white)" stroke-width="1.3" stroke-linecap="round" stroke-linejoin="round">
        <circle cx="552" cy="640" r="4"/><path d="M545,656 q7,-10 14,0 M560,644 h8 v8 h-8z"/>
        <rect x="620" y="690" width="18" height="16"/><path d="M623,695 h12 M623,700 h8 M640,708 l-8,-8"/>
        <rect x="547" y="737" width="18" height="13"/><path d="M551,744 l-2,2 2,2 M556,742 l-2,7"/><circle cx="564" cy="751" r="4"/>
        <path d="M620,786 l9,-5 9,5 -9,5z M620,791 l9,5 9,-5 M620,796 l9,5 9,-5"/>
        <rect x="549" y="830" width="14" height="18"/><path d="M552,836 h8 M552,840 h8 M552,844 h5"/>
        <path d="M621,879 l16,16 M637,879 l-16,16 M619,881 l4,-4 M635,897 l4,-4"/>
        <circle cx="555" cy="932" r="7"/><path d="M560,937 l6,6"/><circle cx="555" cy="932" r="2.5"/>
        <rect x="619" y="978" width="13" height="10"/><path d="M632,981 h5 l3,4 v3 h-8"/><circle cx="623" cy="990" r="2"/><circle cx="636" cy="990" r="2"/>
      </g>
      <g fill="var(--white)">
        <circle cx="581" cy="630" r="8"/><circle cx="607" cy="680" r="8"/>
        <circle cx="557" cy="717" r="8"/><circle cx="629" cy="763" r="8"/>
        <circle cx="557" cy="812" r="8"/><circle cx="629" cy="859" r="8"/>
        <circle cx="557" cy="907" r="8"/><circle cx="649" cy="960" r="8"/>
      </g>
      <g font-family="Outfit, sans-serif" font-size="7" font-weight="700" fill="var(--ink)" text-anchor="middle">
        <text x="581" y="632.5">01</text><text x="607" y="682.5">02</text>
        <text x="557" y="719.5">03</text><text x="629" y="765.5">04</text>
        <text x="557" y="814.5">05</text><text x="629" y="861.5">06</text>
        <text x="557" y="909.5">07</text><text x="649" y="962.5">08</text>
      </g>
    </g>
  </svg>

  <div class="abs brand brand-top">VARNE</div>
  <h1 class="abs headline">Transform your<br>home with Varne<br>design build</h1>
  <p class="abs tagline">Luxury Custom Homes &amp; Major Renovations<br>Built to Reflect Your Vision</p>

  <section>
    <h2 class="abs project-title" style="left:52px;top:474px">Pelwick Kitchen</h2>
    <p class="abs project-caption" style="left:52px;top:500px">A complete kitchen transformation – designed and built by VARNE</p>
    <div class="abs compare" style="left:49px;top:523px;width:280px;height:162px">
      <div class="compare-photo kitchen-before" role="img" aria-label="Kitchen before renovation with dark wood cabinets"><span class="compare-label">BEFORE</span></div>
      <div class="compare-photo kitchen-after" role="img" aria-label="Kitchen after renovation with white cabinets and steel hood"><span class="compare-label">AFTER</span></div>
      <span class="compare-handle">‹ ›</span>
    </div>
  </section>

  <section>
    <h2 class="abs project-title" style="left:42px;top:706px">Exterior</h2>
    <p class="abs project-caption" style="left:42px;top:733px">Exterior elevation updated for curb appeal and modern living"</p>
    <div class="abs compare" style="left:44px;top:757px;width:280px;height:162px">
      <div class="compare-photo exterior-before" role="img" aria-label="Home before renovation"><span class="compare-label">BEFORE</span></div>
      <div class="compare-photo exterior-after" role="img" aria-label="Home exterior after renovation with porch and lawn"><span class="compare-label">AFTER</span></div>
      <span class="compare-handle">‹ ›</span>
    </div>
  </section>

  <h2 class="abs banner-title">Big highlighted<br>box or banner:</h2>
  <p class="abs banner-body">Ready to Build or Transform Your Home? &nbsp; Let<br>VARNE guide you from design to delivery.</p>

  <h2 class="abs process-title">From concept to completion<br>— all under one roof</h2>

  <div class="abs step step-left" style="left:383px;top:625px"><p class="step-name">Initial Consultation</p><p class="step-time">1–2 MONTH</p><p class="step-text">We begin by understanding your vision, preferences, and functional needs, laying…</p></div>
  <div class="abs step" style="left:679px;top:669px"><p class="step-name">Schematic Design</p><p class="step-time">1–2 MONTH</p><p class="step-text">Our architects and designers craft initial layouts and visual concepts, collaborating</p></div>
  <div class="abs step step-left" style="left:383px;top:722px"><p class="step-name">Design Development</p><p class="step-time">1–2 MONTH</p><p class="step-text">We transform initial ideas into detailed plans, refining materials, finishes, and</p></div>
  <div class="abs step" style="left:679px;top:761px"><p class="step-name">Construction Doc...</p><p class="step-time">1 MONTH</p><p class="step-text">Finalized plans &amp; specifications are meticulously reviewed to ensure every</p></div>
  <div class="abs step step-left" style="left:383px;top:820px"><p class="step-name">Permitting</p><p class="step-time">1–3 MONTH</p><p class="step-text">We navigate the permitting process on your behalf, ensuring clear</p></div>
  <div class="abs step" style="left:679px;top:859px"><p class="step-name">Construction</p><p class="step-time">5–18 MONTH</p><p class="step-text">With precision and care, your vision becomes reality. Our Project Manager</p></div>
  <div class="abs step step-left" style="left:383px;top:909px"><p class="step-name">Final Inspection</p><p class="step-time">1–4 WEEK</p><p class="step-text">A detailed walkthrough confirms that every aspect of your new home</p></div>
  <div class="abs step" style="left:679px;top:948px"><p class="step-name">Post Completion</p><p class="step-time">12 MONTHS</p><p class="step-text">A detailed walkthrough confirms that every aspect of your new</p></div>

  <div class="abs brand brand-bottom">VARNE</div>

  <p class="abs contact contact-email">
    <svg width="16" height="12" viewBox="0 0 16 12" aria-hidden="true"><rect x=".5" y=".5" width="15" height="11" fill="none" stroke="#fff"/><path d="M1,1 L8,7 L15,1" fill="none" stroke="#fff"/></svg>
    designsolutions@varne-build.com
  </p>
  <p class="abs contact contact-phone">
    <svg width="14" height="14" viewBox="0 0 24 24" aria-hidden="true"><path d="M6.6 10.8a15.1 15.1 0 0 0 6.6 6.6l2.2-2.2a1 1 0 0 1 1-.25 11.4 11.4 0 0 0 3.6.57 1 1 0 0 1 1 1V20a1 1 0 0 1-1 1A17 17 0 0 1 3 4a1 1 0 0 1 1-1h3.5a1 1 0 0 1 1 1c0 1.25.2 2.45.57 3.6a1 1 0 0 1-.25 1z" fill="none" stroke="#fff" stroke-width="1.5"/></svg>
    555-014-2290
  </p>
</main>
</body>
</html>
```